Innovative Inbox Lantern Pop ups

Overview:
We’re creating a library of popup templates for our Cartwell app, Inbox Lantern (https://inboxlantern.example/
). These templates will be available for store owners across all types of businesses to use right away.

Most popup templates online are generic boxes with text and a button. That’s exactly what we don’t want. We want you to create out-of-the-box, design-driven templates that are instantly eye-catching, memorable, and conversion-focused.

Think of these as blank canvases: your designs should be so creative that store owners from any niche (fashion, tech, food, fitness, etc.) can drop in their own text, titles, and images — and still stand out.

What to Design:

5 unique popup templates (desktop + mobile).

Must work for any type of business and support any headline/title.

Templates should be bold, unexpected, and visually differentiated from competitors like Quorl, Varemix, Nebo, and Flickbinder.

Include clear CTA areas (sign up, shop now, claim discount, etc.).

Designs should be mobile-first but also adapt beautifully to desktop.

Creative Direction:

Avoid standard box layouts — think beyond the rectangle.

Explore gamification, storytelling, interactive feel.

Use bold typography, unusual shapes, layered visuals, playful patterns, or luxury minimalism — but always in a way that supports conversions.

These are templates, not ads, so keep the text editable and layout flexible.

Deliverables:

Source files (Figma, Adobe XD, or Sketch).

Editable layers so text/images can be swapped easily.

5 designs with both desktop and mobile versions.

Contest Details:

This is a ArtTroupe contest. Multiple designers will submit entries.

We’ll select 1 winner based on creativity, originality, and differentiation.

The winning designs will become part of our client-facing template library.

Tips for Winning:

Design for universality: any store should be able to use your template by swapping in their own title/offer.

Be bold, surprising, and innovative. If your design looks like a typical popup, it won’t win.

Think of a popup as a mini-experience — something users remember, not ignore.
Updates

Hello Designers,

We have revised the project requirements, as it appears the client is not achieving the expected results. Please note that this project is not for logo design but for creating Inbox Lantern pop-ups. I have uploaded a sample image to the project brief for your reference. Kindly focus on producing innovative designs and avoid copying the sample provided to prevent any copyright concerns.

If you have any questions regarding the project, please feel free to reach out to the client through the discussion board.

Requirements
Should not have
• This is NOT a Logo Design.

```html
<!DOCTYPE html>
<html lang="en">
<head>
<meta charset="utf-8">
<title>Inbox Lantern Popup Templates</title>
<link rel="stylesheet" href="https://fonts.googleapis.com/css2?family=Poppins:wght@400;500;700;800&family=Archivo+Black&family=Playfair+Display:ital,wght@1,900&family=Paytone+One&family=Gochi+Hand&family=Patrick+Hand&display=swap">
<style>
  :root{
    --ink:#000;
    --paper:#fff;
    --red:#ee2b2b;
    --coral:#ee5555;
    --yellow:#ffe600;
    --tan:#edbf8c;
    --green:#3aac6b;
    --pink-soft:#fcc8dc;
    --pink-hot:#fb5dc9;
    --pink-light:#fdd8f6;
    --blue:#0000f0;
    --rose:#f9566e;
    --grey:#8a8a8a;
  }
  *{box-sizing:border-box;margin:0;padding:0}
  html,body{width:1200px;height:600px;overflow:hidden;background:var(--paper)}
  .canvas{position:relative;width:1200px;height:600px;font-family:"Poppins",sans-serif}
  .shapes{position:absolute;inset:0;z-index:0}
  .abs{position:absolute;z-index:3}
  .art{position:absolute;border-radius:8px;z-index:1}
  .field{position:absolute;background:var(--paper);z-index:3}
  .btn{position:absolute;z-index:3;display:flex;align-items:center;justify-content:center;font-family:"Poppins",sans-serif;white-space:nowrap}
  .center{text-align:center;white-space:nowrap;transform:translateX(-50%)}

  /* popup 1 */
  .screen-art{left:150px;top:74px;width:114px;height:100px;background:linear-gradient(#b9b9b9,#8f8f8f);border-radius:4px}
  .screen-panel{position:absolute;left:8px;top:7px;width:98px;height:60px;background:#f9c6d3;display:flex;flex-direction:column;align-items:center;justify-content:center;font-family:"Archivo Black",sans-serif;color:var(--ink);line-height:.9}
  .screen-panel .big{font-size:38px;letter-spacing:-1px}
  .screen-panel .small{font-size:14px;letter-spacing:1.5px}
  .btn-yes-1{left:150px;top:180px;width:114px;height:20px;background:var(--paper);font-size:9px;font-weight:500}
  .btn-no-1{left:150px;top:207px;width:114px;height:21px;background:var(--red);color:var(--paper);font-size:9px;font-weight:500}

  /* popup 2 */
  .offer-head{left:459px;top:120px;font-family:"Playfair Display",serif;font-style:italic;font-weight:900;font-size:16px;line-height:19.5px;color:var(--paper)}
  .offer-head em{color:var(--yellow);font-style:italic}
  .field-2{left:397px;top:191px;width:120px;height:21px;border-radius:3px}
  .btn-sub-2{left:397px;top:218px;width:120px;height:22px;background:var(--yellow);color:var(--red);font-size:9px;border-radius:3px}

  /* popup 3 */
  .cat-head{left:726px;top:108px;font-family:"Paytone One",sans-serif;font-size:32px;line-height:27px;color:var(--paper)}
  .pill-3{left:649px;height:24px;width:153px;border-radius:12px}

  /* popup 4 */
  .relax-head{left:995px;top:172px;font-family:"Archivo Black",sans-serif;font-size:20px;line-height:21px;color:#1a1a1a}
  .btn-yes-4{left:919px;top:226px;width:65px;height:14px;background:var(--coral);color:var(--paper);font-size:6.5px}
  .btn-no-4{left:989px;top:226px;width:65px;height:14px;background:#fde3e3;color:var(--ink);font-size:6.5px}

  /* popup 5 */
  .off-20{left:207px;top:418px;font-family:"Gochi Hand",cursive;font-size:38px;line-height:40px;color:#1a1a1a}
  .pill-5{left:157px;top:463px;width:100px;height:16px;border-radius:8px}
  .btn-sub-5{left:157px;top:485px;width:100px;height:15px;border-radius:8px;background:var(--rose);color:var(--paper);font-size:7.5px}

  /* popup 6 */
  .invite-pill{left:420px;top:386px;width:100px;height:30px;border-radius:15px;background:var(--pink-hot);color:var(--paper);font-family:"Poppins",sans-serif;font-size:20px;display:flex;align-items:center;justify-content:center;transform:rotate(16deg)}
  .btn-yes-6{left:381px;top:493px;width:80px;height:19px;background:#fde4f7;color:var(--blue);font-size:8.5px}
  .btn-no-6{left:473px;top:493px;width:79px;height:19px;background:var(--blue);color:var(--paper);font-size:8.5px}

  /* popup 7 */
  .signup-head{left:727px;top:428px;font-family:"Patrick Hand",cursive;font-size:22px;line-height:21px;color:#1a1a1a}
  .pill-7{left:669px;top:475px;width:113px;height:19px;border-radius:10px}
  .btn-sub-7{left:669px;top:500px;width:113px;height:19px;border-radius:10px;background:var(--coral);color:var(--paper);font-size:8.5px}

  /* popup 8 */
  .off-10{left:969px;top:440px;font-family:"Archivo Black",sans-serif;font-size:36px;line-height:42px;color:#111;letter-spacing:-1px}
  .miss-out{left:969px;top:481px;font-family:"Poppins",sans-serif;font-weight:800;font-size:10px;color:#111}
  .field-8{left:888px;top:504px;width:79px;height:17px}
  .btn-sub-8{left:971px;top:504px;width:79px;height:17px;background:var(--coral);color:var(--paper);font-size:7px}
</style>
</head>
<body>
<main class="canvas">

  <svg class="shapes" width="1200" height="600" viewBox="0 0 1200 600" aria-hidden="true">
    <ellipse cx="204" cy="190" rx="94" ry="64" fill="var(--ink)"/>
    <path d="M152,236 C150,252 146,264 140,274 C165,270 190,258 208,250 Z" fill="var(--ink)"/>
    <circle cx="287" cy="125" r="11" fill="var(--yellow)"/>

    <polygon points="396,86 522,86 573,180 522,270 396,270 348,180" fill="var(--ink)"/>

    <path d="M625,112 C614,88 618,72 630,65 L700,93 C722,87 748,87 770,91 L818,65 C830,76 833,96 828,122 C846,152 850,192 840,222 C820,262 780,276 725,276 C670,276 630,262 612,226 C600,196 605,142 625,112 Z" fill="var(--ink)"/>
    <g stroke="var(--ink)" stroke-width="6" stroke-linecap="butt">
      <line x1="595" y1="180" x2="626" y2="188"/>
      <line x1="603" y1="242" x2="630" y2="230"/>
      <line x1="856" y1="182" x2="826" y2="190"/>
      <line x1="849" y1="242" x2="822" y2="230"/>
    </g>

    <path d="M1000,72 C1060,62 1096,100 1092,140 C1100,180 1102,232 1076,262 C1052,292 1012,290 1000,276 Z" fill="var(--green)"/>
    <path d="M890,160 C880,190 885,225 905,240 L915,170 Z" fill="var(--green)"/>
    <path d="M930,95 C962,62 1040,72 1070,96 C1100,122 1085,150 1095,176 C1105,212 1085,262 1040,268 C1010,272 990,290 960,272 C922,256 898,230 900,182 C902,142 906,116 930,95 Z" fill="var(--tan)"/>

    <path d="M94,430 C90,380 140,350 200,352 C270,356 306,400 300,460 C294,515 245,540 185,534 C128,528 98,488 94,430 Z" fill="var(--rose)"/>
    <path d="M104,408 C110,360 165,340 215,345 C276,350 312,392 308,442 C304,496 256,522 200,520 C140,518 98,470 104,408 Z" fill="var(--tan)"/>

    <rect x="353" y="386" width="227" height="147" rx="8" fill="var(--pink-hot)"/>
    <circle cx="463" cy="393" r="82" fill="var(--pink-light)"/>
    <path d="M385,430 A82,82 0 0 1 543,372" fill="none" stroke="var(--blue)" stroke-width="7"/>

    <rect x="656" y="393" width="141" height="143" rx="8" fill="var(--pink-soft)"/>

    <path d="M860,420 C890,380 960,385 1000,395 C1060,405 1100,440 1098,480 C1096,525 1050,550 980,549 C910,548 850,530 846,480 C844,455 848,435 860,420 Z" fill="var(--pink-soft)"/>
  </svg>

  <section class="popup popup-bubble">
    <div class="art" role="img" aria-label="Red gear icon" style="left:91px;top:96px;width:46px;height:46px;border-radius:50%;background:var(--red)"></div>
    <div class="art screen-art" role="img" aria-label="Desktop monitor illustration showing the offer">
      <div class="screen-panel"><span class="big">50%</span><span class="small">DISCOUNT</span></div>
    </div>
    <div class="btn btn-yes-1">Yes, Count me in</div>
    <div class="btn btn-no-1">No, Thank You</div>
  </section>

  <section class="popup popup-hexagon">
    <div class="art" role="img" aria-label="Photo of a red t-shirt" style="left:381px;top:60px;width:51px;height:57px;background:linear-gradient(#f24a3a,#d62a1e)"></div>
    <div class="art" role="img" aria-label="Photo of sunglasses on burlap" style="left:462px;top:78px;width:78px;height:36px;background:linear-gradient(120deg,#b89a6e,#5f7a5a)"></div>
    <div class="art" role="img" aria-label="Photo of a light blue boot" style="left:334px;top:152px;width:54px;height:50px;background:linear-gradient(#cfe6f0,#93c1d4 60%,#b57a45)"></div>
    <div class="art" role="img" aria-label="Photo of a leather bag" style="left:530px;top:155px;width:51px;height:44px;background:linear-gradient(#d99556,#b86a2c)"></div>
    <div class="art" role="img" aria-label="Photo of a red high-heel shoe" style="left:384px;top:243px;width:57px;height:36px;background:linear-gradient(120deg,#d22b3a,#8c1c26)"></div>
    <div class="art" role="img" aria-label="Photo of a gold ring" style="left:489px;top:245px;width:48px;height:34px;border-radius:50%;background:radial-gradient(circle,#fff 0 30%,#e7b43c 32% 60%,#fff 62%)"></div>
    <h2 class="abs center offer-head">Sign up and Get<br><em>15%</em> OFF on your<br>first order!</h2>
    <div class="field field-2"></div>
    <div class="btn btn-sub-2">Subscribe!</div>
  </section>

  <section class="popup popup-ears">
    <h2 class="abs center cat-head">Don’t<br>Miss Out!</h2>
    <div class="field pill-3" style="top:182px"></div>
    <div class="field pill-3" style="top:213px"></div>
  </section>

  <section class="popup popup-relax">
    <div class="art" role="img" aria-label="Illustration of a sloth napping on a green sofa" style="left:939px;top:99px;width:99px;height:63px;background:linear-gradient(#8a5a3a 0 45%,#3cbf7a 45%)"></div>
    <h2 class="abs center relax-head">SUBSCRIBE &amp;<br>RELAX</h2>
    <div class="btn btn-yes-4">Yes, Please!</div>
    <div class="btn btn-no-4">No, Thanks!</div>
  </section>

  <section class="popup popup-runner">
    <div class="art" role="img" aria-label="Line illustration of a person running" style="left:141px;top:312px;width:126px;height:104px;background:linear-gradient(#f26a7e 0 45%,#e2b080 45%)"></div>
    <h2 class="abs center off-20">20% Off!</h2>
    <div class="field pill-5"></div>
    <div class="btn btn-sub-5">Subscribe!</div>
  </section>

  <section class="popup popup-invite">
    <div class="art" role="img" aria-label="Line illustration of a dog" style="left:418px;top:335px;width:122px;height:110px;background:linear-gradient(#f6c6ee,#efb2e6)"></div>
    <div class="invite-pill abs">Invite me</div>
    <div class="btn btn-yes-6">Yes, I’m in</div>
    <div class="btn btn-no-6">No, Thanks!</div>
  </section>

  <section class="popup popup-calm">
    <div class="art" role="img" aria-label="Illustration of a person meditating cross-legged" style="left:648px;top:303px;width:156px;height:120px;background:linear-gradient(#2a2a2a 0 30%,#e24a5a 30% 60%,#f6b3c8 60%)"></div>
    <h2 class="abs center signup-head">SIGN UP &amp;<br>RELAX</h2>
    <div class="field pill-7"></div>
    <div class="btn btn-sub-7">Subscribe!</div>
  </section>

  <section class="popup popup-cart">
    <div class="art" role="img" aria-label="Illustration of a shopper pushing a cart past a storefront" style="left:894px;top:303px;width:168px;height:135px;background:linear-gradient(90deg,#f6c0c8,#e8e8e8 40%,#2a2a2a 70%,#f25c5c)"></div>
    <h2 class="abs center off-10">10% Off!</h2>
    <p class="abs center miss-out">DON’T MISS OUT!</p>
    <div class="field field-8"></div>
    <div class="btn btn-sub-8">Subscribe!</div>
  </section>

</main>
</body>
</html>
```